Personal letterhead and stationary

I am looking for someone to design letterhead and stationary set for my personal use. I want something simple and timeless with a little bit of color. I like photography, computers and writing.

```html
<!DOCTYPE html>
<html lang="en">
<head>
<meta charset="utf-8">
<title>Gabriel Lee Hayes — Personal Stationery</title>
<link rel="stylesheet" href="https://fonts.googleapis.com/css2?family=EB+Garamond:ital,wght@0,400;1,400&display=swap">
<style>
  :root {
    --ink: #0d0d0d;
    --accent: #e8433a;
    --canvas: #ffffff;
    --paper: #fcfcfa;
    --paper-edge: #c9c9c9;
  }
  * { margin: 0; padding: 0; box-sizing: border-box; }
  html, body {
    width: 1200px;
    height: 1000px;
    overflow: hidden;
    background: var(--canvas);
  }
  .canvas {
    position: relative;
    width: 1200px;
    height: 1000px;
    overflow: hidden;
    color: var(--ink);
    font-family: "EB Garamond", Georgia, serif;
  }

  /* Identity lockup, large */
  .lockup {
    position: absolute;
    left: 100px;
    top: 178px;
    width: 1020px;
  }
  .lockup .name {
    font-style: italic;
    font-weight: 400;
    font-size: 82px;
    line-height: 1;
    letter-spacing: 0.085em;
    white-space: nowrap;
  }
  .lockup .address {
    display: flex;
    align-items: center;
    margin-top: 40px;
    font-size: 24px;
    letter-spacing: 0.14em;
    white-space: nowrap;
  }
  .lockup .marker {
    width: 18px;
    height: 18px;
    background: var(--accent);
    margin-right: 18px;
    flex: none;
  }

  /* Letterhead sheet */
  .sheet {
    position: absolute;
    left: 647px;
    top: 493px;
    width: 469px;
    height: 560px;
    background: var(--paper);
    border: 1px solid var(--paper-edge);
  }
  .sheet .head {
    position: absolute;
    left: 51px;
    top: 38px;
  }
  .sheet .name {
    font-style: italic;
    font-weight: 400;
    font-size: 30px;
    line-height: 1;
    letter-spacing: 0.085em;
    white-space: nowrap;
  }
  .sheet .address {
    display: flex;
    align-items: center;
    margin-top: 13px;
    font-size: 9.6px;
    letter-spacing: 0.12em;
    white-space: nowrap;
  }
  .sheet .marker {
    width: 7px;
    height: 7px;
    background: var(--accent);
    margin-right: 6px;
    flex: none;
  }
</style>
</head>
<body>
  <main class="canvas">
    <section class="lockup">
      <h1 class="name">GABRIEL LEE HAYES</h1>
      <p class="address"><span class="marker"></span>2450 Harbor View Lane, San Leandro, California 94577</p>
    </section>

    <article class="sheet">
      <header class="head">
        <h2 class="name">GABRIEL LEE HAYES</h2>
        <p class="address"><span class="marker"></span>2450 Harbor View Lane, San Leandro, California 94577</p>
      </header>
    </article>
  </main>
</body>
</html>
```